FR / EN Beekeeper research design packaging / label; Beekeeper looking for a design package

I need as a beekeeper to create a design to better showcase my honey. Indeed I work in a natural environment of high quality on a hill called "Veldmoor" (many flowers different fields, few pesticides, ...). I practice a beekeeping respectful of the bee and in a traditional way. I produce a high quality honey (luxury product) for a wealthy clientele looking for good health products, ... The main label should contain only the following text (accompanied by an image): The Veldmoor Honey A variant would also be useful for my production of mead (alcohol from the fermentation of honey): The Veldmoor mead In terms of form, given the target audience, I thought I was moving towards a modern label against a background black and with golden patterns. An example is the honey of the wonders attached, we find a honey assimilated as a real luxury product. Same in the Cuvée Lando Perrusi attachment. I would like to move towards these tones of colors by adding a touch more "champêtre" as on the label of the bottle of wine below where one sees golden flowers drawn, of light and subtle way. Another example that I like is that of the bee of ree joined. Another modern idea identified on this site is this design: https://www.artpitchhub.com/design/30418822 https: //www.artpitchhub. com / design / 30418957 I would also need a round label to place on the lid of the pot with indications of signs (my address) as well as additional information about my product: - BALDUCCI Armand - Veldmoor, 14 - 6812 Hautvelin - 500 g - Spring harvest - Honey all flowers - Flora: rapeseed, fruit trees, clovers - Flavors: sweet honey with vegetal notes Remarks: this is my first artpitchhub project, if you are surprised by some points of the brief or it is missing important information do not hesitate to let me know! ************************************************** ******************************* ENGLISH ****************** ************** I need to beekeeper a new design Indeed, I work in a very natural environment, a high quality eco-system which is the south of Belgium (many different flowers in the fields, few pesticides, ...). I practice a natural beekeeping, in an artisanal way I produce a high quality honey (luxuous product) for wealthy people who are looking for good and healthy products. The following description: The Veldmoor Honey A slight variation could be useful for my production (alcohol from honey fermentation): The Veldmoor Meads Concerning the form, a modern design with golden patterns on a black background could be appropriate. An example is the honey of the wonders in attachment, we could see that honey in this case is a branded like a very luxuous product. I wish to go for these last colors with a more "rural touch" as attachment. We can see golden flowers in a light and elegant manner. Another interesting example is the honey bee in attachment. Some example found on this site: https://www.artpitchhub.com/design/30418822 https: //www.artpitchhub. com / design / 30418957 Balducci Armand - Veldmoor, 14 - 6812 Hautvelin - 500 g - Spring Harvest - Honey all flowers - Flora: rapeseed, fruit, clovers - Flavors: sweet honey with vegetal notes

Target Market(s)

affluent clientele looking for natural products, good for health, ...

Industry/Entity Type

Agriculture

Font styles to use
Decorative
Script
Other font styles liked:
• à la libre appréciation du designer, tant que c'est moderne et élégant

Requirements
Must have
• All text must be in French / A main label and a round label on the lid of the jar. Gilding (preferably on a black background). An image accompanying the text. Gold on a black background
Nice to have
• Elegant and modern design Elegant and modern design
Should not have
• Do not load too much the main label, it must remain uncluttered

```html
<!DOCTYPE html>
<html lang="fr">
<head>
<meta charset="utf-8">
<title>Le miel du Veldmoor — étiquettes</title>
<link rel="stylesheet" href="https://fonts.googleapis.com/css2?family=Cormorant+Garamond:wght@500;600&family=Roboto+Condensed:wght@400&display=swap">
<style>
  :root {
    --paper: #ffffff;
    --label-black: #0b0b0b;
    --gold: #b8995a;
    --gold-light: #d9c49a;
    --ink: #1a1a1a;
    --guide: #8a8a8a;
  }
  html, body { margin: 0; padding: 0; overflow: hidden; background: var(--paper); }
  .sheet { display: block; width: 1200px; height: 699px; }
  .brand-name { font-family: "Cormorant Garamond", Georgia, serif; font-weight: 600; fill: var(--gold); }
  .tagline { font-family: "Cormorant Garamond", Georgia, serif; font-weight: 500; fill: var(--gold); letter-spacing: 1.2px; }
  .details { font-family: "Cormorant Garamond", Georgia, serif; font-weight: 600; fill: #ffffff; font-size: 10px; }
  .address { font-family: "Cormorant Garamond", Georgia, serif; font-weight: 600; fill: #ffffff; font-size: 10.5px; letter-spacing: 0.3px; }
  .dimension-text { font-family: "Roboto Condensed", Arial, sans-serif; font-size: 19px; fill: var(--ink); }
  .caption { font-family: "Roboto Condensed", Arial, sans-serif; font-size: 27px; fill: var(--ink); }
  .dim-line { stroke: var(--ink); stroke-width: 1; fill: none; }
  .guide-line { stroke: var(--guide); stroke-width: 0.8; stroke-dasharray: 3 3; fill: none; }
  .stitch { stroke: var(--gold); stroke-width: 1; stroke-dasharray: 4 3; fill: none; }
</style>
</head>
<body>
<svg class="sheet" viewBox="0 0 1200 699" xmlns="http://www.w3.org/2000/svg">
  <defs>
    <marker id="arrow" viewBox="0 0 10 10" refX="10" refY="5" markerWidth="8" markerHeight="8" orient="auto-start-reverse">
      <path d="M0,1 L10,5 L0,9 Z" fill="#1a1a1a"/>
    </marker>
    <path id="address-arc" d="M -103,0 A 103 103 0 0 0 103,0"/>
    <linearGradient id="floral-tone" x1="0" y1="0" x2="0" y2="1">
      <stop offset="0" stop-color="#e9dcbf"/>
      <stop offset="1" stop-color="#cdb27a"/>
    </linearGradient>
  </defs>

  <!-- Spring lid label -->
  <g class="lid-label spring">
    <rect x="221" y="340" width="63" height="234" fill="var(--label-black)"/>
    <line class="stitch" x1="228" y1="352" x2="228" y2="572"/>
    <line class="stitch" x1="277" y1="352" x2="277" y2="572"/>
    <g transform="translate(253,226)">
      <circle r="130" fill="var(--gold)"/>
      <circle r="119" fill="var(--label-black)"/>
      <circle r="112" class="stitch"/>
      <text class="brand-name" x="0" y="-70" font-size="15" text-anchor="middle">Le miel du</text>
      <text class="brand-name" x="0" y="-44" font-size="28" text-anchor="middle">Veldmoor</text>
      <text class="tagline" x="0" y="7" font-size="10.5" text-anchor="middle">MIEL DOUX AUX NOTES VÉGÉTALES</text>
      <line x1="-101" y1="15" x2="101" y2="15" stroke="var(--gold)" stroke-width="1"/>
      <text class="details" text-anchor="middle">
        <tspan x="0" y="31">Récolte de printemps | Miel toutes fleurs</tspan>
        <tspan x="0" y="43">Flore : brassicacées, fruitiers, trèfle</tspan>
        <tspan x="0" y="55">Saveurs : miel doux aux</tspan>
        <tspan x="0" y="67">notes végétales</tspan>
        <tspan x="0" y="81" font-size="8">- 500 g -</tspan>
      </text>
      <text class="address"><textPath href="#address-arc" startOffset="50%" text-anchor="middle">BALDUCCI Armand | Veldmoor, 14 | 6812 Hautvelin</textPath></text>
    </g>
  </g>

  <!-- Summer lid label -->
  <g class="lid-label summer">
    <rect x="956" y="340" width="62" height="234" fill="var(--label-black)"/>
    <line class="stitch" x1="963" y1="352" x2="963" y2="572"/>
    <line class="stitch" x1="1011" y1="352" x2="1011" y2="572"/>
    <g transform="translate(988,226)">
      <circle r="130" fill="var(--gold)"/>
      <circle r="119" fill="var(--label-black)"/>
      <circle r="112" class="stitch"/>
      <text class="brand-name" x="0" y="-70" font-size="15" text-anchor="middle">Le miel du</text>
      <text class="brand-name" x="0" y="-44" font-size="28" text-anchor="middle">Veldmoor</text>
      <text class="tagline" x="0" y="7" font-size="10.5" text-anchor="middle">MIEL DOUX AUX NOTES VÉGÉTALES</text>
      <line x1="-101" y1="15" x2="101" y2="15" stroke="var(--gold)" stroke-width="1"/>
      <text class="details" text-anchor="middle">
        <tspan x="0" y="31">Récolte d’été | Miel toutes fleurs</tspan>
        <tspan x="0" y="43">Flore : ronces, trèfle, fruitiers, tilleul</tspan>
        <tspan x="0" y="55">Saveurs : miel doux aux</tspan>
        <tspan x="0" y="67">notes végétales</tspan>
        <tspan x="0" y="81" font-size="8">- 500 g -</tspan>
      </text>
      <text class="address"><textPath href="#address-arc" startOffset="50%" text-anchor="middle">BALDUCCI Armand | Veldmoor, 14 | 6812 Hautvelin</textPath></text>
    </g>
  </g>

  <!-- Main jar label -->
  <g class="main-label">
    <rect x="486" y="328" width="318" height="90" fill="url(#floral-tone)" opacity="0.55" role="img" aria-label="Golden drawn wildflowers and scrolling foliage"/>
    <rect x="486" y="418" width="318" height="12" fill="var(--gold)"/>
    <path d="M486,430 H804 V540 Q804,550 794,550 H496 Q486,550 486,540 Z" fill="var(--label-black)"/>
    <text class="brand-name" x="645" y="455" font-size="19" text-anchor="middle">Le miel du</text>
    <text class="brand-name" x="645" y="490" font-size="36" text-anchor="middle">Veldmoor</text>
    <text class="tagline" x="645" y="522" font-size="12" text-anchor="middle">MIEL DOUX AUX NOTES VÉGÉTALES</text>
  </g>

  <!-- Dimension guides -->
  <g class="dimensions">
    <line class="guide-line" x1="123" y1="42" x2="123" y2="200"/>
    <line class="guide-line" x1="382" y1="42" x2="382" y2="200"/>
    <line class="dim-line" x1="123" y1="58" x2="382" y2="58" marker-start="url(#arrow)" marker-end="url(#arrow)"/>
    <text class="dimension-text" x="264" y="49" text-anchor="middle">6.5 cm.</text>

    <line class="guide-line" x1="58" y1="97" x2="216" y2="97"/>
    <line class="guide-line" x1="58" y1="356" x2="218" y2="356"/>
    <line class="guide-line" x1="58" y1="574" x2="218" y2="574"/>
    <line class="dim-line" x1="74" y1="97" x2="74" y2="352" marker-start="url(#arrow)" marker-end="url(#arrow)"/>
    <line class="dim-line" x1="74" y1="358" x2="74" y2="574" marker-start="url(#arrow)" marker-end="url(#arrow)"/>
    <text class="dimension-text" transform="translate(65,226) rotate(-90)" text-anchor="middle">6.5 cm.</text>
    <text class="dimension-text" transform="translate(65,465) rotate(-90)" text-anchor="middle">5.5 cm.</text>

    <line class="guide-line" x1="486" y1="283" x2="486" y2="332"/>
    <line class="guide-line" x1="804" y1="283" x2="804" y2="332"/>
    <line class="dim-line" x1="486" y1="293" x2="804" y2="293" marker-start="url(#arrow)" marker-end="url(#arrow)"/>
    <text class="dimension-text" x="658" y="284" text-anchor="middle">8 cm.</text>

    <line class="guide-line" x1="418" y1="332" x2="482" y2="332"/>
    <line class="guide-line" x1="418" y1="550" x2="482" y2="550"/>
    <line class="dim-line" x1="434" y1="332" x2="434" y2="550" marker-start="url(#arrow)" marker-end="url(#arrow)"/>
    <text class="dimension-text" transform="translate(425,440) rotate(-90)" text-anchor="middle">5.5 cm.</text>
  </g>

  <text class="caption" x="242" y="636" text-anchor="middle">SPRING HONEY</text>
  <text class="caption" x="980" y="636" text-anchor="middle">SUMMER HONEY</text>
</svg>
</body>
</html>
```